Infographic for Anesthesia Management Company

I would like my Anesthesia Management company, Verity Sedation, service information placed into a infographic for use on a brochure and webpage. Please focus on just the infographic.
-Verity Services text to be placed into infographic attached in word file.
-Two Vector infographic templates attached as well. I am open to either option, or alternative layout suggestion.
-Please match color scheme to veritysedation.com
-Verity logo attached.
Thank you for your help!
Todd
Target Market(s)
Surgery Centers
Industry/Entity Type
It Company
Font styles to use
Requirements
Must have
- Professional Look.
- Easy to read text.
- Cohesive branding
Nice to have
- Please see attached Vector examples.

```html
<!DOCTYPE html>
<html lang="en">
<head>
<meta charset="utf-8">
<title>Verity Sedation – Service Infographic</title>
<link href="https://fonts.googleapis.com/css2?family=Montserrat:wght@300;400;600;700&family=Open+Sans:wght@400;600&display=swap" rel="stylesheet">
<style>
  :root{
    --red:#e3262a; --red-dark:#b3151a;
    --grey-light:#b9b9bb; --grey-light-dark:#8c8c8f;
    --grey:#7a7a7d; --grey-dark:#545457;
    --teal:#1fa58a; --teal-dark:#137a66;
    --ink:#2b2b2b; --text:#555; --rule:#3a3a3a;
    --bg:#ffffff;
  }
  *{margin:0;padding:0;box-sizing:border-box}
  html,body{width:1200px;height:900px;overflow:hidden;background:var(--bg)}
  .infographic{position:relative;width:1200px;height:900px;overflow:hidden;background:var(--bg);font-family:"Open Sans",sans-serif;color:var(--text)}
  .shelf{position:absolute;height:2px;background:linear-gradient(to right,rgba(0,0,0,0),rgba(0,0,0,.12));}
  .tab{position:absolute;width:140px;height:300px;color:#fff;text-align:center;font-family:"Montserrat",sans-serif;box-shadow:6px 8px 14px rgba(0,0,0,.22)}
  .tab::before{content:"";position:absolute;left:0;top:0;width:100%;height:34px;background:rgba(255,255,255,.16);clip-path:polygon(0 0,100% 0,100% 100%,0 20%)}
  .tab-letter{display:block;font-size:60px;font-weight:700;line-height:1;margin-top:44px}
  .tab-label{display:block;font-size:12px;font-weight:600;letter-spacing:.06em;text-transform:uppercase;margin-top:10px}
  .tab-icon{position:absolute;left:45px;bottom:46px;width:50px;height:50px}
  .tab--d{left:150px;top:190px;background:linear-gradient(135deg,var(--red),var(--red-dark))}
  .tab--c{left:300px;top:280px;background:linear-gradient(135deg,var(--grey-light),var(--grey-light-dark))}
  .tab--b{left:450px;top:370px;background:linear-gradient(135deg,var(--grey),var(--grey-dark))}
  .tab--a{left:600px;top:460px;background:linear-gradient(135deg,var(--teal),var(--teal-dark))}
  .service{position:absolute;font-size:10.5px;line-height:13.5px}
  .service h3{font-family:"Montserrat",sans-serif;font-size:13px;font-weight:700;color:var(--ink);line-height:16px}
  .service ol,.service ul{padding-left:16px}
  .service--d{left:304px;top:186px;width:560px}
  .service--c{left:454px;top:276px;width:520px}
  .service--b{left:604px;top:362px;width:500px}
  .service--a{left:754px;top:464px;width:400px}
  .brand-rule{position:absolute;left:750px;top:456px;width:400px;height:2px;background:var(--rule)}
  .brand{position:absolute;left:790px;top:600px;display:flex;align-items:center;gap:12px;font-family:"Montserrat",sans-serif;font-weight:600;font-size:38px;color:var(--teal)}
  .brand-dot{width:22px;height:22px;border-radius:50%;background:var(--teal)}
  .footer-rule{position:absolute;left:90px;top:800px;width:1020px;height:3px;background:linear-gradient(to right,var(--red) 0 35%,var(--rule) 35% 100%)}
  .tagline{position:absolute;left:90px;top:820px;width:1020px;text-align:center;font-family:"Montserrat",sans-serif;font-weight:300;font-size:23px;letter-spacing:.02em;color:var(--teal);text-transform:uppercase;white-space:nowrap}
</style>
</head>
<body>
<main class="infographic">
  <div class="shelf" style="left:20px;top:540px;width:130px"></div>
  <div class="shelf" style="left:20px;top:590px;width:280px"></div>
  <div class="shelf" style="left:20px;top:680px;width:430px"></div>
  <div class="shelf" style="left:20px;top:750px;width:580px"></div>

  <div class="tab tab--d">
    <span class="tab-letter">D</span><span class="tab-label">Patient Safety</span>
    <svg class="tab-icon" viewBox="0 0 50 50" fill="none" stroke="#fff" stroke-width="2"><circle cx="25" cy="25" r="23"/><rect x="16" y="23" width="18" height="13" rx="2" fill="#fff"/><path d="M19 23v-5a6 6 0 0 1 12 0v5"/></svg>
  </div>
  <div class="tab tab--c">
    <span class="tab-letter">C</span><span class="tab-label">Efficiency</span>
    <svg class="tab-icon" viewBox="0 0 50 50" fill="none" stroke="#fff" stroke-width="2"><circle cx="25" cy="25" r="23"/><circle cx="25" cy="27" r="10"/><path d="M25 27v-6M22 14h6M25 14v3"/></svg>
  </div>
  <div class="tab tab--b">
    <span class="tab-letter">B</span><span class="tab-label">Accountability</span>
    <svg class="tab-icon" viewBox="0 0 50 50" fill="none" stroke="#fff" stroke-width="2"><circle cx="25" cy="25" r="23"/><rect x="15" y="16" width="18" height="18"/><path d="M18 24l5 5 12-14" stroke-width="3"/></svg>
  </div>
  <div class="tab tab--a">
    <span class="tab-letter">A</span><span class="tab-label">Professionalism</span>
    <svg class="tab-icon" viewBox="0 0 50 50" fill="none" stroke="#fff" stroke-width="2"><circle cx="25" cy="25" r="23"/><path d="M12 24l6-6 7 3 7-3 6 6M18 22l8 9 3-2M22 26l5 5M26 23l6 6"/></svg>
  </div>

  <section class="service service--d">
    <h3>Clinical Guidance and Quality Improvement</h3>
    <p>Verity implements clinical guidelines to ensure patient safety and satisfaction, including:</p>
    <ol>
      <li>Pre-operative guideline protocols to minimize cancellations and optimize patient outcomes</li>
      <li>Patient selection criteria to ensure suitable surgical candidates</li>
      <li>Education programs to engage the clinical staff</li>
      <li>Evidence-based multimodal pain management protocol to facilitate timely discharges and reduce side effects</li>
    </ol>
  </section>
  <section class="service service--c">
    <h3>Thought Leadership</h3>
    <ul>
      <li>Staff-free anesthesia services</li>
      <li>Proprietary and data-driven process to improve surgery flow</li>
      <li>Verity's clinical processes empower its anesthesia providers to help the surgery center team excel in the perioperative setting</li>
    </ul>
  </section>
  <section class="service service--b">
    <h3>In-House Billing</h3>
    <ul>
      <li>Verity streamlines the billing process</li>
      <li>We have dedicated staff that ensures all claims are processed correctly the first time</li>
    </ul>
    <h3>Meeting Accreditation Requirements</h3>
    <ul>
      <li>Verity partners with your surgery center to ensure all things pertaining to anesthesia are up to current ASC credentialing standards</li>
    </ul>
  </section>
  <div class="brand-rule"></div>
  <section class="service service--a">
    <h3>ASC Stakeholder Satisfaction</h3>
    <ul>
      <li>Verity draws its personnel from a network of highly qualified anesthesia providers</li>
      <li>We strive to create continuity between anesthesia, surgeon, and ASC staff</li>
      <li>Provide ample staffing according to your scheduled case volume</li>
      <li>Verity guarantees every anesthesia provider upholds clinical excellence</li>
    </ul>
  </section>

  <div class="brand"><span class="brand-dot"></span>Verity Sedation</div>

  <div class="footer-rule"></div>
  <p class="tagline">Anesthesia Provider Recruitment, Credentialing, and Staffing</p>
</main>
</body>
</html>
```